Cocktail Bar Aperitivo Promotion

I need a flyer designed for my aperitivo promotion. Aperitivo is an Italian tradition much like the cocktail hour where you can relax and unwind over a drink and a little snack.
Bramble Toots a unique and fun 1950’s style bar - a relaxed local meeting place, the kind of bar where your bartender drinks on their night off. The final design should reflect the enthusiastic spirit of the 1950s cocktail culture as well as the fun, summery Italian vibe of the aperitvo and it needs to highlight the 2 aperitivo cocktails on offer, their price and the time of the promotion. Please also include the logo, address, phone number and website.
Negronis $16
Vellaro Spritz $14
All share plates $10
From 4pm - 6pm every day
Address: 472 Wexcombe Rd Wexcombe
Phone: 8153 2947
brambletoots.com.au
Please also refer to our website- brambletoots.com.au for a sense of who we are and what we do.

```html
<!DOCTYPE html>
<html lang="en">
<head>
<meta charset="utf-8">
<title>Bramble Toots – Aperitivo Flyer</title>
<link href="https://fonts.googleapis.com/css2?family=Arimo:wght@700&family=Yellowtail&display=swap" rel="stylesheet">
<style>
  :root {
    --page-bg: #e9e4dc;
    --peach: #fdd99d;
    --peach-footer: #fcd596;
    --charcoal: #232123;
    --ink: #2b2a2c;
    --cream-script: #f8d89c;
    --white: #ffffff;
    --rule: #d9d4cc;
  }
  * { box-sizing: border-box; margin: 0; padding: 0; }
  html, body {
    width: 934px; height: 1200px; overflow: hidden;
    background: var(--page-bg);
  }
  .flyer {
    position: absolute; left: 163px; top: 167px;
    width: 609px; height: 865px;
    background: var(--charcoal);
    box-shadow: 0 6px 18px rgba(0,0,0,.25);
    font-family: "Arimo", Arial, sans-serif;
  }
  .masthead {
    position: absolute; left: 0; top: 0; width: 100%; height: 158px;
    background: var(--peach);
  }
  .brand-name {
    position: absolute; right: 60px; top: 52px;
    font-weight: 700; font-size: 38px; line-height: 1;
    color: var(--ink); text-align: right; letter-spacing: .5px;
  }
  .bar-photo {
    position: absolute; left: 0; top: 158px; width: 100%; height: 402px;
    background:
      linear-gradient(180deg, rgba(60,45,40,.0) 55%, rgba(30,30,30,.35) 100%),
      linear-gradient(100deg, #8fae8a 0%, #a7c09d 22%, #b8453a 38%, #c9a37a 55%, #5d5f66 75%, #8d6a4a 100%);
  }
  .promo {
    position: absolute; left: 0; top: 560px; width: 100%; height: 248px;
  }
  .cocktail-art {
    position: absolute; left: 42px; top: 8px; width: 165px; height: 210px;
    background: radial-gradient(ellipse at 45% 45%, #e9c3b3 0%, #c9d98a 35%, rgba(35,33,35,0) 70%);
  }
  .menu {
    position: absolute; left: 228px; top: 22px; width: 345px;
    list-style: none;
  }
  .menu-item {
    display: flex; align-items: baseline; height: 45px;
    color: var(--cream-script);
  }
  .menu-item .dish {
    font-family: "Yellowtail", cursive; font-size: 34px; white-space: nowrap;
  }
  .menu-item .leader {
    flex: 1; overflow: hidden; white-space: nowrap;
    font-family: "Yellowtail", cursive; font-size: 34px;
  }
  .menu-item .price {
    font-weight: 700; font-size: 31px; padding-left: 2px;
  }
  .hours {
    position: absolute; left: 230px; top: 171px; width: 347px; height: 30px;
    border-top: 1px solid var(--rule); border-bottom: 1px solid var(--rule);
    color: var(--white); font-weight: 700; font-size: 20.5px;
    line-height: 28px; text-align: center; letter-spacing: .2px;
  }
  .address {
    position: absolute; left: 226px; top: 224px; width: 350px;
    color: var(--peach); font-weight: 700; font-size: 14.5px;
    text-align: center; letter-spacing: .3px;
  }
  .contact-bar {
    position: absolute; left: 0; top: 808px; width: 100%; height: 57px;
    background: var(--peach-footer);
    display: flex; justify-content: flex-end; align-items: center;
    padding-right: 35px; gap: 6px;
    color: var(--ink); font-weight: 700; font-size: 19px;
  }
  .contact-bar .item { display: flex; align-items: center; gap: 6px; }
  .contact-bar svg { width: 19px; height: 19px; display: block; }
</style>
</head>
<body>
  <main class="flyer">
    <header class="masthead">
      <div class="brand-name">Bramble<br>Toots</div>
    </header>

    <div class="bar-photo" role="img" aria-label="Photo of the retro 1950s bar interior with green cabinets, red tiles, red stools and a checkered floor"></div>

    <section class="promo">
      <div class="cocktail-art" role="img" aria-label="Illustration of two coupe cocktail glasses with sparkles"></div>

      <ul class="menu">
        <li class="menu-item"><span class="dish">Negronis</span><span class="leader">..........................................</span><span class="price">$16</span></li>
        <li class="menu-item"><span class="dish">Vellaro Spritz</span><span class="leader">..........................................</span><span class="price">$14</span></li>
        <li class="menu-item"><span class="dish">All share plates</span><span class="leader">..........................................</span><span class="price">$10</span></li>
      </ul>

      <p class="hours">FROM 4PM - 6PM EVERY DAY</p>
      <p class="address">472 WEXCOMBE RD WEXCOMBE</p>
    </section>

    <footer class="contact-bar">
      <span class="item">
        <svg viewBox="0 0 20 20" aria-hidden="true"><rect x="1" y="1" width="18" height="18" rx="4" fill="#2b2a2c"/><path d="M7 5.5c-.8.4-1.3 1.3-1 2.6.6 2.6 2.5 5 4.6 6.2 1 .6 2 .4 2.6-.3l.4-.6-1.9-1.5-.8.8c-1-.5-2.2-2-2.6-3.2l.9-.6-1-2.1z" fill="#fcd596"/></svg>
        8153 2947
      </span>
      <span class="item">
        <svg viewBox="0 0 20 20" aria-hidden="true"><rect x="1" y="1" width="18" height="18" rx="4" fill="#2b2a2c"/><rect x="4.5" y="6" width="11" height="8" fill="#fcd596"/><path d="M4.5 6l5.5 4.5L15.5 6" fill="none" stroke="#2b2a2c" stroke-width="1.2"/></svg>
        brambletoots.com.au
      </span>
    </footer>
  </main>
</body>
</html>
```